Lanternby Consulting Business Card Design

Business Card Design for Lanternby Consulting. Lanternby Consulting is a boutique consultancy based in Atlanta, GA., that specializes in marketing strategy, organization planning, and leadership development. We provide solutions for small businesses and startups as well as Meridex 400 companies.

http://lanternbyconsulting.example/

Target Market(s)

We provide solutions for small businesses and startups as well as Meridex 400 companies.

Industry/Entity Type

Consulting

Contact Information for Business Card

Two sided business card with priority on contact information, logo, tag line (Guidance to Plan Better, Lead Better, Grow Further)

Colors

Designer to choose colors to be used in the design.

Requirements
Must have
• contact information, logo, tag line (Guidance to Plan Better, Lead Better, Grow Further)
• Simple no over communication.
Nice to have
• I would like to see different placements of logo and creative use of both sides of the card
Should not have
• Do not put too much information on the card.

```html
<!DOCTYPE html>
<html lang="en">
<head>
<meta charset="utf-8">
<title>Lanternby Consulting – Business Card</title>
<link href="https://fonts.googleapis.com/css2?family=Roboto:ital,wght@0,300;0,400;0,500;1,700&display=swap" rel="stylesheet">
<style>
  :root {
    --backdrop: #2b2b2b;
    --card: #3a3a3a;
    --band: #0c0c0c;
    --silver-light: #e6e6e6;
    --silver-dark: #9a9a9a;
    --front-mark: #6e6e6e;
    --ink-light: #ffffff;
  }
  * { margin: 0; padding: 0; box-sizing: border-box; }
  html, body {
    width: 799px;
    height: 1200px;
    overflow: hidden;
    background: var(--backdrop);
    font-family: "Roboto", Arial, sans-serif;
  }
  .canvas {
    position: relative;
    width: 799px;
    height: 1200px;
  }
  .card {
    position: absolute;
    left: 90px;
    width: 620px;
    height: 355px;
    background: var(--card);
    border-radius: 26px;
    overflow: hidden;
    box-shadow: 0 18px 30px rgba(0,0,0,0.45);
  }
  .card--front { top: 120px; }
  .card--back { top: 720px; }

  .wordmark {
    display: flex;
    align-items: center;
    gap: 14px;
    font-weight: 500;
    letter-spacing: 1px;
    white-space: nowrap;
  }
  .wordmark__dot {
    width: 16px;
    height: 16px;
    border-radius: 50%;
    background: currentColor;
    flex: none;
  }
  .card--front .wordmark {
    position: absolute;
    left: 0; right: 0; top: 150px;
    justify-content: center;
    font-size: 42px;
    color: var(--front-mark);
  }
  .card--back .wordmark {
    position: absolute;
    left: 80px; top: 52px;
    font-size: 36px;
    color: var(--ink-light);
  }

  .holder-name {
    position: absolute;
    left: 70px; top: 148px;
    font-size: 22px;
    font-style: italic;
    font-weight: 700;
    color: var(--ink-light);
  }
  .contact {
    position: absolute;
    left: 320px; top: 198px;
    list-style: none;
    font-size: 16px;
    line-height: 1.4;
    color: var(--ink-light);
    white-space: nowrap;
  }
  .band {
    position: absolute;
    left: 0; bottom: 0;
    width: 620px;
    height: 80px;
  }
  .tagline {
    position: absolute;
    left: 250px; right: 16px; bottom: 18px;
    font-size: 15px;
    color: var(--ink-light);
    text-align: center;
    white-space: nowrap;
  }
</style>
</head>
<body>
<main class="canvas">
  <section class="card card--front" aria-label="Card front">
    <div class="wordmark"><span class="wordmark__dot"></span>Lanternby Consulting</div>
  </section>

  <section class="card card--back" aria-label="Card back">
    <div class="wordmark"><span class="wordmark__dot"></span>Lanternby Consulting</div>
    <p class="holder-name">Devon</p>
    <ul class="contact">
      <li>404-555-0192</li>
      <li>devon@lanternbyconsulting.example</li>
      <li>www.lanternbyconsulting.example</li>
    </ul>
    <svg class="band" viewBox="0 0 620 80" aria-hidden="true">
      <defs>
        <linearGradient id="silver" x1="0" y1="0" x2="1" y2="1">
          <stop offset="0" stop-color="#e6e6e6"/>
          <stop offset="1" stop-color="#9a9a9a"/>
        </linearGradient>
      </defs>
      <polygon points="0,10 248,10 232,50 0,50" fill="url(#silver)"/>
      <polygon points="232,80 250,22 620,22 620,80" fill="#0c0c0c"/>
    </svg>
    <p class="tagline">Guidance to Plan Better, Lead Better, Grow Further</p>
  </section>
</main>
</body>
</html>
```